A4 Flyer

Bright Path Learning is starting a course in regional Victoria. We are currently advertising (See attached file A34984) in local papers but need to create a one page flyer to distribute to Aged Care facilities in the area. The A4 flyer will be inserted into a folder pack with more detailed information on Bright Path Learning. Important to use images and logoes attached

Target Market(s)

Flyer to be distributed to Aged Care facility staff and owners

Industry/Entity Type

Advertising

Font styles to use
Sans Serif

Colors
f37123
ec1f27

Requirements
Must have
• BPL Logo
Some image

```html
<!DOCTYPE html>
<html lang="en">
<head>
<meta charset="utf-8">
<title>Bright Path Learning – Fast Track Course Flyer</title>
<link rel="stylesheet" href="https://fonts.googleapis.com/css2?family=Arimo:wght@400;700&family=Open+Sans:wght@400;700&display=swap">
<style>
  :root {
    --brand-orange: #f37123;
    --brand-red: #ec1f27;
    --banner-orange: #ef5325;
    --ink: #1a1a1a;
    --ink-soft: #333333;
    --logo-grey: #4a4a4a;
    --panel: #ffffff;
    --pill-top: #f2f2f2;
    --pill-bottom: #d9d9d9;
    --bullet: #6d6d6d;
  }
  * { margin: 0; padding: 0; box-sizing: border-box; }
  html, body { width: 900px; height: 1200px; overflow: hidden; }
  body { background: #ffffff; font-family: "Arimo", Arial, sans-serif; }

  .flyer {
    position: relative;
    width: 900px;
    height: 1200px;
    background: var(--brand-orange);
    overflow: hidden;
  }

  .headline {
    position: absolute; top: 14px; left: 0; width: 100%;
    text-align: center; color: #fff;
    font-size: 66px; font-weight: 400; line-height: 1;
  }
  .start-date {
    position: absolute; top: 104px; left: 0; width: 100%;
    text-align: center; color: #fff; font-size: 23px;
  }

  .content-panel {
    position: absolute; left: 14px; top: 170px;
    width: 872px; height: 928px;
    background: var(--panel);
  }

  .brand-lockup {
    position: absolute; left: 40px; top: 188px;
    display: flex; align-items: center; gap: 26px;
  }
  .brand-dot {
    width: 96px; height: 96px; border-radius: 50%;
    background: var(--brand-orange);
  }
  .brand-name {
    color: var(--logo-grey);
    font-size: 50px; font-weight: 700; line-height: 1.05;
    letter-spacing: 1px;
  }

  .venue-pill {
    position: absolute; left: 638px; top: 180px;
    width: 228px; height: 114px;
    border-radius: 30px;
    background: linear-gradient(var(--pill-top), var(--pill-bottom));
    box-shadow: 0 3px 3px rgba(0,0,0,0.25);
    padding: 14px 0 0 17px;
    color: var(--ink); font-size: 21px; line-height: 28px;
  }

  .qualification-banner {
    position: absolute; left: 30px; top: 320px;
    width: 838px; height: 115px;
    border-radius: 32px;
    background: linear-gradient(var(--banner-orange), #e84c22);
    color: #fff; text-align: center;
    font-size: 24px; font-weight: 700; line-height: 31px;
    padding-top: 27px; letter-spacing: 0.3px;
  }

  .funding-note {
    position: absolute; left: 85px; top: 450px;
    font-size: 21px; color: #000;
  }

  .photo {
    position: absolute; top: 535px; height: 252px;
    border-radius: 8px;
  }
  .photo--student-man { left: 28px; width: 266px; background: linear-gradient(160deg, #eef0f2, #c9ccd0); }
  .photo--student-woman { left: 320px; width: 258px; background: linear-gradient(160deg, #e9eaec, #5a4a44); }
  .photo--anatomy-model { left: 604px; width: 265px; background: linear-gradient(160deg, #d8e6f0, #d9a58e); }

  .funding-statement {
    position: absolute; left: 0; top: 814px; width: 900px;
    text-align: center; font-family: "Open Sans", Verdana, sans-serif;
    font-size: 24px; line-height: 36px; color: var(--ink-soft);
  }
  .funding-statement strong { color: var(--ink); }

  .course-units {
    position: absolute; top: 911px;
    list-style: none; font-size: 24px; line-height: 34px; color: #000;
  }
  .course-units--left { left: 28px; }
  .course-units--right { left: 519px; }
  .course-units li { display: flex; align-items: center; gap: 18px; }
  .course-units svg { width: 16px; height: 16px; flex: none; }

  .enrol {
    position: absolute; left: 0; top: 1102px; width: 900px;
    text-align: center; color: #fff;
    font-size: 23px; line-height: 31px;
  }
</style>
</head>
<body>
<svg width="0" height="0" style="position:absolute">
  <defs>
    <symbol id="cog-bullet" viewBox="0 0 16 16">
      <g fill="var(--bullet)">
        <rect x="7" y="1" width="2" height="14"/>
        <rect x="1" y="7" width="14" height="2"/>
        <rect x="7" y="1" width="2" height="14" transform="rotate(45 8 8)"/>
        <rect x="7" y="1" width="2" height="14" transform="rotate(-45 8 8)"/>
        <circle cx="8" cy="8" r="5"/>
      </g>
      <circle cx="8" cy="8" r="2" fill="#fff"/>
    </symbol>
  </defs>
</svg>

<main class="flyer">
  <h1 class="headline">Unique Opportunity!</h1>
  <p class="start-date">Fast Track Course - Start July 2014</p>

  <section class="content-panel"></section>

  <div class="brand-lockup">
    <span class="brand-dot"></span>
    <span class="brand-name">bright path<br>learning</span>
  </div>

  <div class="venue-pill">Hillcrest Nursing<br>Home - Westbrook<br>9:00am - 3:00pm</div>

  <div class="qualification-banner">DOUBLE QUALIFICATION - CERT III IN AGED CARE WITH<br>HOME AND COMMUNITY CARE</div>

  <p class="funding-note">Government Funding for eligible students! Fees from&nbsp; $117</p>

  <div class="photo photo--student-man" role="img" aria-label="Photo of a smiling mature student in a white shirt seated in a classroom"></div>
  <div class="photo photo--student-woman" role="img" aria-label="Photo of a young student in a black top seated with hands clasped in a classroom"></div>
  <div class="photo photo--anatomy-model" role="img" aria-label="Photo of a trainer demonstrating on an anatomical torso model"></div>

  <p class="funding-statement">This Training is Delliverd With <strong>Vic and Comm</strong><br><strong>Govt Funding</strong> To Eligble students</p>

  <ul class="course-units course-units--left">
    <li><svg><use href="#cog-bullet"/></svg>Pathology</li>
    <li><svg><use href="#cog-bullet"/></svg>Anaphylaxis</li>
    <li><svg><use href="#cog-bullet"/></svg>Mediacaions of PCA’s</li>
    <li><svg><use href="#cog-bullet"/></svg>Aged Care</li>
  </ul>
  <ul class="course-units course-units--right">
    <li><svg><use href="#cog-bullet"/></svg>Home &amp; Community Care</li>
    <li><svg><use href="#cog-bullet"/></svg>CPR</li>
    <li><svg><use href="#cog-bullet"/></svg>First Aid</li>
    <li><svg><use href="#cog-bullet"/></svg>Health Services</li>
  </ul>

  <p class="enrol">to enrol visit<br>brightpathlearning.com.au<br>or call 9555 0142</p>
</main>
</body>
</html>
```